Redesign of existing business card

I would like the "signage" attachment converted into a business card. This needs to be double sided aswell, keeping the phone number and names on the front, and the email + website on the back.

Second attachment is the current business card design.

Larger font for contact details is required.

Must keep to original color themes (electric blue, silver/grey etc)

Back of the card to have blue background with white writing.

Industry/Entity Type

Business

Contact Information for Business Card

Refer to existing design from attachments

Requirements
Must have
• Refer to existing design from attachments
Nice to have

```html
<!DOCTYPE html>
<html lang="en">
<head>
<meta charset="UTF-8">
<title>Voltara Electrical Services – Business Card</title>
<link href="https://fonts.googleapis.com/css2?family=Roboto+Condensed:wght@400;700&display=swap" rel="stylesheet">
<style>
  :root {
    --electric-blue: #283593;
    --silver: #a7abb1;
    --grey-text: #5d6169;
    --paper: #ffffff;
    --backdrop: #eceef0;
    --white-text: #ffffff;
  }
  * { box-sizing: border-box; margin: 0; padding: 0; }
  html, body {
    width: 1200px;
    height: 800px;
    overflow: hidden;
  }
  body {
    background: var(--backdrop);
    font-family: "Roboto Condensed", "Arial Narrow", sans-serif;
    display: flex;
    align-items: center;
    justify-content: center;
    gap: 60px;
  }
  .card {
    position: relative;
    width: 520px;
    height: 300px;
    background: var(--paper);
    box-shadow: 0 6px 18px rgba(0, 0, 0, 0.12);
    overflow: hidden;
  }
  .card__band {
    position: absolute;
    inset: 0;
    width: 100%;
    height: 100%;
  }
  .card__band polygon { fill: var(--electric-blue); }
  .brand {
    position: absolute;
    top: 36px;
    left: 28px;
    display: flex;
    align-items: center;
    gap: 12px;
  }
  .brand__dot {
    width: 48px;
    height: 48px;
    border-radius: 50%;
    background: var(--silver);
    flex: none;
  }
  .brand__name {
    font-size: 22px;
    font-weight: 700;
    text-transform: uppercase;
    letter-spacing: 0.3px;
    color: var(--electric-blue);
    white-space: nowrap;
  }
  .card__tag {
    position: absolute;
    top: 92px;
    right: 125px;
    font-size: 15px;
    font-weight: 400;
    color: var(--grey-text);
    white-space: nowrap;
  }
  .contact {
    position: absolute;
    left: 120px;
    top: 205px;
    list-style: none;
    color: var(--white-text);
    font-size: 27px;
    font-weight: 400;
    line-height: 1.3;
    white-space: nowrap;
  }
  .contact--back {
    left: 96px;
    top: 210px;
    font-size: 23px;
  }
</style>
</head>
<body>

  <section class="card card--front">
    <svg class="card__band" viewBox="0 0 520 300" preserveAspectRatio="none" aria-hidden="true">
      <polygon points="0,215 440,150 458,140 470,105 484,114 496,70 508,78 520,40 520,300 0,300"/>
    </svg>
    <div class="brand">
      <span class="brand__dot"></span>
      <span class="brand__name">Voltara Electrical Services</span>
    </div>
    <p class="card__tag">Daniel Harper</p>
    <ul class="contact">
      <li>M: 9999 318 420</li>
      <li>P: 0400 318 420</li>
    </ul>
  </section>

  <section class="card card--back">
    <svg class="card__band" viewBox="0 0 520 300" preserveAspectRatio="none" aria-hidden="true">
      <polygon points="0,215 440,150 458,140 470,105 484,114 496,70 508,78 520,40 520,300 0,300"/>
    </svg>
    <div class="brand">
      <span class="brand__dot"></span>
      <span class="brand__name">Voltara Electrical Services</span>
    </div>
    <p class="card__tag">EC 20473</p>
    <ul class="contact contact--back">
      <li>daniel@voltaraelectrical.com.au</li>
      <li>www.voltaraelectrical.com.au</li>
    </ul>
  </section>

</body>
</html>
```